International Parcel Forwarder needs website redesign and logo

We need an updated website design to make our existing site look more modern, global and trustworthy. Current site
www.parvento.com -- we do not want to rebuild headers or at this point do copyright we are simply looking to make the site pop:)
The service we provide is for shoppers living outside the USA looking to shop here and save money on shipping or get access to stores that won't ship internationally or accept international payment.
Target Market(s)
Online shoppers living outside the USA
Industry/Entity Type
Shipping
Logo Text
US shopping, global shipping
Coding
Coded - Design and coding required
Number of Pages Required
5+ page
Font styles to use

```html
<!DOCTYPE html>
<html lang="en">
<head>
<meta charset="utf-8">
<title>parvento — US shopping, global shipping</title>
<link rel="stylesheet" href="https://fonts.googleapis.com/css2?family=Cabin:wght@400;500;700&family=Open+Sans:wght@400;600&display=swap">
<style>
:root{
  --orange:#f7941d;
  --navy:#232c38;
  --navy-deep:#1b222c;
  --ink:#2b2b2b;
  --muted:#777;
  --line:#e2e2e2;
  --soft:#f7f7f7;
  --strip:#eef3f9;
  --white:#fff;
  --tick:#8cc63f;
}
*{box-sizing:border-box;margin:0;padding:0}
html,body{width:1200px;height:3125px;overflow:hidden}
body{font-family:"Open Sans",Arial,sans-serif;color:var(--ink);background:var(--white);position:relative}
.topbar{height:42px;background:var(--navy);display:flex;padding-left:58px}
.topbar a{display:flex;align-items:center;padding:0 22px;color:var(--white);font-size:13px;text-decoration:none}
.topbar .login{background:var(--orange)}
.header{height:100px;display:flex;align-items:center;justify-content:space-between;padding:0 52px;border-bottom:1px solid var(--line)}
.brand{display:flex;align-items:center;gap:12px}
.brand-mark{width:56px;height:56px;background:var(--navy)}
.brand-name{font-family:"Cabin",sans-serif;font-weight:700;font-size:44px;color:var(--ink);line-height:1}
.brand-tag{font-family:"Cabin",sans-serif;font-weight:700;font-size:11px;color:var(--ink);margin-top:2px}
.nav{display:flex;gap:44px;height:100px}
.nav a{display:flex;align-items:center;font-size:13px;color:var(--ink);text-decoration:none;position:relative}
.nav a.active::after{content:"";position:absolute;left:-8px;right:-8px;bottom:0;height:4px;background:var(--navy)}
.hero{position:relative;height:625px;background:linear-gradient(180deg,#6f9fcf 0%,#b9d1e6 40%,#9a9fa6 62%,#6d7075 100%);display:flex;align-items:center;justify-content:center}
.hero h1{font-family:"Cabin",sans-serif;font-weight:500;font-size:38px;color:var(--white);text-align:center;line-height:1.35;text-shadow:0 2px 6px rgba(0,0,0,.5)}
.hero .arrow{position:absolute;top:258px;width:50px;height:88px;background:rgba(255,255,255,.85);display:flex;align-items:center;justify-content:center}
.hero .arrow.left{left:0}.hero .arrow.right{right:0}
.section-title{font-family:"Cabin",sans-serif;font-weight:400;font-size:30px;text-align:center;color:var(--ink)}
.rule{width:96px;height:2px;background:var(--orange);margin:16px auto 0}
.welcome{height:312px;padding-top:78px}
.welcome p{width:960px;margin:40px auto 0;text-align:center;font-size:12.5px;line-height:18px;color:var(--muted)}
.how{height:467px;background:var(--soft);padding-top:70px}
.steps{display:flex;margin:82px 0 0 12px}
.step{width:294px;text-align:center;border-right:1px solid var(--line);height:205px}
.step:last-child{border-right:none}
.step svg{display:block;margin:0 auto}
.step p{font-size:14px;line-height:18px;color:var(--ink);margin-top:20px;width:220px;margin-left:auto;margin-right:auto}
.band{height:504px;background:var(--navy);position:relative}
.video{position:absolute;left:67px;top:83px;width:470px;height:350px;border:6px solid var(--white);border-radius:6px;background:linear-gradient(160deg,#f4d35e 0%,#e8b84a 45%,#3b8fc9 100%)}
.checklist{position:absolute;left:621px;top:112px;list-style:none}
.checklist li{display:flex;align-items:center;gap:14px;color:var(--white);font-size:14px;height:37px}
.btn{position:absolute;left:587px;top:375px;width:157px;height:37px;background:var(--orange);color:var(--white);font-size:13px;display:flex;align-items:center;justify-content:center;text-transform:uppercase}
.why{height:550px;padding-top:70px;position:relative}
.why .divider{position:absolute;left:598px;width:1px;background:var(--line)}
.feature{position:absolute;display:flex;gap:22px}
.feature h3{font-size:15px;font-weight:600;color:var(--ink);margin:10px 0 6px;text-transform:uppercase}
.feature li{list-style:none;font-size:14px;line-height:19px;color:var(--muted)}
.feature li::before{content:"• ";color:var(--orange)}
.brands{height:191px;background:var(--strip);display:flex;align-items:center;justify-content:space-between;padding:0 50px}
.brands .logos{display:flex;gap:64px;align-items:center}
.brands span{font-family:"Cabin",sans-serif;font-size:38px;color:#666;font-weight:500}
.footer{height:292px;background:var(--navy);position:relative;color:var(--white)}
.col{position:absolute;top:66px}
.col h4{font-family:"Cabin",sans-serif;font-weight:500;font-size:18px;margin-bottom:14px}
.col a,.col p{display:block;font-size:14px;line-height:20px;color:var(--white);text-decoration:none}
.col .phone{font-size:19px;margin-bottom:6px}
.input{width:205px;height:28px;background:var(--white);font-size:10px;color:#aaa;padding:8px 12px}
.sub{width:80px;height:24px;background:var(--orange);font-size:9px;display:flex;align-items:center;justify-content:center;margin:10px 0 0 122px}
.socials{display:flex;gap:8px}
.socials i{width:28px;height:28px;border-radius:50%;display:block}
.copy{position:absolute;left:0;bottom:0;width:1200px;height:42px;background:var(--navy-deep);color:var(--white);font-size:12px;display:flex;align-items:center;padding-left:90px}
</style>
</head>
<body>
<div class="topbar"><a class="login">Login</a><a>Sign Up</a></div>
<header class="header">
  <div class="brand">
    <div class="brand-mark"></div>
    <div><div class="brand-name">parvento</div><div class="brand-tag">US shopping, global shipping</div></div>
  </div>
  <nav class="nav">
    <a class="active">Shipping Calculator</a><a>How It Works</a><a>Parvento Pricing</a><a>Learn More</a><a>Blog</a><a>Contact Us</a>
  </nav>
</header>
<section class="hero" role="img" aria-label="Cargo jet on an airport apron with wrapped freight pallets under a blue sky">
  <div class="arrow left"><svg width="14" height="22"><path d="M11 3 3 11l8 8" fill="none" stroke="#333" stroke-width="2.5"/></svg></div>
  <h1>Shop at any U.S. retailer.<br>Ship anywhere.</h1>
  <div class="arrow right"><svg width="14" height="22"><path d="M3 3l8 8-8 8" fill="none" stroke="#333" stroke-width="2.5"/></svg></div>
</section>
<section class="welcome">
  <h2 class="section-title">welcome to parvento</h2>
  <div class="rule"></div>
  <p>Parvento is a leading company in the Package Forwarding industry. By leveraging the latest technologies and relationships with the world's top international shippers, Parvento provides tools to make shopping stores in the USA as easy as shopping at home. Whether you are shopping the USA for that new tablet for your business in Argentina or picking up some new fashions from your home in Paris, Parvento provides easy access to USA merchants. Once your purchases are shipped to your personal USA Address, provided by Parvento, we expedite delivery of products to your doorstep.</p>
</section>
<section class="how">
  <h2 class="section-title">how parvento works</h2>
  <div class="steps">
    <div class="step">
      <svg width="150" height="136" viewBox="0 0 150 136"><circle cx="70" cy="68" r="64" fill="var(--navy)"/><path d="M128 60l12 8-12 8z" fill="var(--navy)"/>
        <g fill="#fff"><rect x="40" y="48" width="62" height="4"/><rect x="40" y="56" width="62" height="4"/><rect x="40" y="64" width="62" height="4"/><rect x="40" y="72" width="62" height="4"/><rect x="40" y="80" width="62" height="4"/><rect x="40" y="48" width="26" height="20"/></g></svg>
      <p>Register for your free U.S. shopping address</p>
    </div>
    <div class="step">
      <svg width="150" height="136" viewBox="0 0 150 136"><circle cx="70" cy="68" r="64" fill="var(--navy)"/><path d="M128 60l12 8-12 8z" fill="var(--navy)"/>
        <g fill="none" stroke="#fff" stroke-width="3"><circle cx="66" cy="64" r="24"/><ellipse cx="66" cy="64" rx="10" ry="24"/><path d="M42 64h48M46 52h40M46 76h40"/><path d="M78 80h6l4 14h16l3-10h-21"/></g><circle cx="92" cy="99" r="2.5" fill="#fff"/><circle cx="102" cy="99" r="2.5" fill="#fff"/></svg>
      <p>Shop anywhere in the U.S</p>
    </div>
    <div class="step">
      <svg width="150" height="136" viewBox="0 0 150 136"><circle cx="70" cy="68" r="64" fill="var(--navy)"/><path d="M128 60l12 8-12 8z" fill="var(--navy)"/>
        <path d="M70 38 40 64h8v26h16V74h12v16h16V64h8z" fill="#fff"/></svg>
      <p>Parvento receives your package and you get notified automatically</p>
    </div>
    <div class="step">
      <svg width="150" height="136" viewBox="0 0 150 136"><circle cx="70" cy="68" r="64" fill="var(--navy)"/><path d="M128 60l12 8-12 8z" fill="var(--navy)"/>
        <path d="M40 74l8-2 10 6 14-6-12-16 6-2 20 13 14-5c5-2 8 2 3 5l-14 7-6 20-6 2v-17l-20 9-16-2z" fill="#fff"/></svg>
      <p>You choose how to ship your package anywhere in the world</p>
    </div>
  </div>
</section>
<section class="band">
  <div class="video" role="img" aria-label="Illustrated explainer video of a couple shopping on a laptop, with a play button"></div>
  <ul class="checklist">
    <li><svg width="14" height="12"><path d="M1 6l4 4 8-9" fill="none" stroke="var(--tick)" stroke-width="2"/></svg>Sign up with Parvento and get your own address for shopping in the USA</li>
    <li><svg width="14" height="12"><path d="M1 6l4 4 8-9" fill="none" stroke="var(--tick)" stroke-width="2"/></svg>Shop in the U.S.</li>
    <li><svg width="14" height="12"><path d="M1 6l4 4 8-9" fill="none" stroke="var(--tick)" stroke-width="2"/></svg>Parvento receives your package</li>
    <li><svg width="14" height="12"><path d="M1 6l4 4 8-9" fill="none" stroke="var(--tick)" stroke-width="2"/></svg>Manage your packages in our Parvento app</li>
    <li><svg width="14" height="12"><path d="M1 6l4 4 8-9" fill="none" stroke="var(--tick)" stroke-width="2"/></svg>Tell us how you want it shipped</li>
    <li><svg width="14" height="12"><path d="M1 6l4 4 8-9" fill="none" stroke="var(--tick)" stroke-width="2"/></svg>Track your shipment</li>
  </ul>
  <div class="btn">Signup Today</div>
</section>
<section class="why">
  <h2 class="section-title">why use parvento</h2>
  <div class="rule"></div>
  <div class="divider" style="top:168px;height:110px"></div>
  <div class="divider" style="top:330px;height:110px"></div>
  <div class="feature" style="left:56px;top:170px">
    <svg width="98" height="98" viewBox="0 0 98 98"><circle cx="49" cy="49" r="47" fill="var(--navy)"/><circle cx="49" cy="49" r="40" fill="none" stroke="#fff" stroke-width="2"/><path d="M33 52v-6a16 16 0 0 1 32 0v6" fill="none" stroke="#fff" stroke-width="4"/><rect x="29" y="48" width="8" height="14" rx="3" fill="#fff"/><rect x="61" y="48" width="8" height="14" rx="3" fill="#fff"/><circle cx="49" cy="52" r="10" fill="#fff"/></svg>
    <div><h3>Experience</h3><ul><li>30 years experience in international shipping.</li><li>Excellent customer service</li></ul></div>
  </div>
  <div class="feature" style="left:652px;top:170px">
    <svg width="98" height="98" viewBox="0 0 98 98"><circle cx="49" cy="49" r="47" fill="var(--navy)"/><circle cx="49" cy="49" r="28" fill="none" stroke="#fff" stroke-width="4"/><text x="49" y="60" text-anchor="middle" fill="#fff" font-family="Cabin,sans-serif" font-size="32" font-weight="700">$</text></svg>
    <div><h3>Value</h3><ul><li>Discounted shipping rates with major carriers</li><li>No membership or joining fees</li><li>Low consolidation fees</li></ul></div>
  </div>
  <div class="feature" style="left:56px;top:332px">
    <svg width="98" height="98" viewBox="0 0 98 98"><circle cx="49" cy="49" r="47" fill="var(--navy)"/><path d="M49 70 28 50a12 12 0 0 1 21-16 12 12 0 0 1 21 16z" fill="none" stroke="#fff" stroke-width="3"/></svg>
    <div><h3>Trust</h3><ul><li>Excellent customer service</li><li>A+ rating from the Trusted Commerce Council</li></ul></div>
  </div>
  <div class="feature" style="left:652px;top:332px">
    <svg width="98" height="98" viewBox="0 0 98 98"><circle cx="49" cy="49" r="47" fill="var(--navy)"/><g fill="#fff"><ellipse cx="49" cy="34" rx="18" ry="6"/><path d="M31 40c0 4 8 6 18 6s18-2 18-6v7c0 4-8 6-18 6s-18-2-18-6z"/><path d="M31 52c0 4 8 6 18 6s18-2 18-6v7c0 4-8 6-18 6s-18-2-18-6z"/></g></svg>
    <div><h3>Savings</h3><ul><li>No fees to receive packages</li><li>No U.S. sales tax when using our<br>New Hampshire warehouse</li><li>45 days free storage</li></ul></div>
  </div>
</section>
<section class="brands">
  <svg width="16" height="28"><path d="M13 2 3 14l10 12" fill="none" stroke="#666" stroke-width="2"/></svg>
  <div class="logos"><span>littlebloom</span><span>marketly</span><span>TRENDLINE</span><span>VELVET HUE</span><span>HALLSTEAD</span></div>
  <svg width="16" height="28"><path d="M3 2l10 12L3 26" fill="none" stroke="#666" stroke-width="2"/></svg>
</section>
<footer class="footer">
  <div class="col" style="left:92px"><h4>QUICK LINKS</h4><a>How it works</a><a>Pricing</a><a>Terms of Service</a><a>Privacy Policy</a><a>Contact Us</a></div>
  <div class="col" style="left:325px"><h4>CONTACT US</h4><p class="phone">555-014-2290</p><p>E: info@parvento.com</p><p>A: 42 Harbor Crest Rd.<br>Dunmore, MN 55990</p></div>
  <div class="col" style="left:658px"><h4>CONTACT US</h4><div class="input">Enter your Message</div><div class="sub">SUBSCRIBE</div></div>
  <div class="col" style="left:965px"><h4>SOCIAL MEDIA</h4><div class="socials"><i style="background:#3b5998"></i><i style="background:#3aa0e0"></i><i style="background:#a8896b"></i><i style="background:#d9493a"></i></div></div>
  <div class="copy">Copyright 2017 parvento All Rights Reserved.</div>
</footer>
</body>
</html>
```